Velvet Harbor for sale at the 2019 Tandor Crest Mare Auction on 30 May 2019

I am selling my broodmare at the 2019 Tandor Crest Mare auction on 30 May 2019. I need a flyer to hand out to potential buyers. I have included the required information in the attached word document. I can provide more images if required. I am thinking that a DL double sided or an A5 will suit best. I'm happy to provide more information as required.

Target Market(s)

Race horse breeders, people who buy broodmares.

Font styles to use
Serif
Sans Serif
Script

Colors

Designer to choose colors to be used in the design.

Requirements
Must have
• All of the content provided in the attached brief, however it is not necessary to have the words exactly as per the brief. The brief is for information purposes.
Nice to have
• Innovation...

```html
<!DOCTYPE html>
<html lang="en">
<head>
<meta charset="utf-8">
<title>Velvet Harbor – Race Record</title>
<link href="https://fonts.googleapis.com/css2?family=Montserrat:wght@700;800&family=Roboto+Condensed:wght@700&display=swap" rel="stylesheet">
<style>
  :root {
    --band: rgba(12, 12, 12, 0.86);
    --band-label: #0b0b0b;
    --accent: #f2e600;
    --text: #ffffff;
    --sky: #f4f4f2;
    --rail: #c9ccd0;
    --stand: #5a6470;
    --turf: #3f7a3a;
    --turf-dark: #28552a;
  }
  * { margin: 0; padding: 0; box-sizing: border-box; }
  html, body { width: 847px; height: 1200px; overflow: hidden; background: #ffffff; }
  .flyer {
    position: relative;
    width: 847px;
    height: 1200px;
    overflow: hidden;
  }
  .racecourse-photo {
    position: absolute;
    inset: 0;
    background:
      linear-gradient(180deg,
        var(--sky) 0%,
        #dfe3e0 10%,
        var(--rail) 22%,
        #8c96a0 38%,
        var(--stand) 52%,
        #4a5a52 66%,
        var(--turf) 80%,
        var(--turf-dark) 100%);
  }
  .results {
    position: absolute;
    inset: 0;
  }
  .result {
    position: absolute;
    left: 76px;
    width: 743px;
    display: flex;
    background: var(--band);
  }
  .result__label {
    position: relative;
    width: 320px;
    flex: none;
    background: var(--band-label);
    padding-left: 116px;
    padding-right: 16px;
    display: flex;
    align-items: center;
  }
  .result__label::before {
    content: "";
    position: absolute;
    left: 0;
    top: 0;
    bottom: 0;
    width: 22px;
    background: var(--accent);
  }
  .result__headline {
    font-family: "Montserrat", sans-serif;
    font-weight: 800;
    font-size: 20px;
    line-height: 1.3;
    color: var(--text);
    text-transform: uppercase;
  }
  .result__details {
    display: flex;
    align-items: center;
    padding: 0 24px 0 36px;
    font-family: "Roboto Condensed", sans-serif;
    font-weight: 700;
    font-size: 17px;
    line-height: 1.3;
    color: var(--text);
    text-transform: uppercase;
  }
</style>
</head>
<body>
<main class="flyer">
  <div class="racecourse-photo" role="img" aria-label="Racecourse photograph with horses racing past the rails and grandstand signage"></div>

  <section class="results">
    <article class="result" style="top:102px; height:166px;">
      <div class="result__label"><h2 class="result__headline">Velvet Harbor<br>wins by 3.5L</h2></div>
      <p class="result__details">Class 6 Handicap – 1400m<br>Ridgewater Racing Club<br>(Kestrel Park),<br>21 January 2017</p>
    </article>

    <article class="result" style="top:322px; height:192px;">
      <div class="result__label"><h2 class="result__headline">Velvet Harbor<br>wins by 2.8L</h2></div>
      <p class="result__details">No more than one metro win<br>handicap – 1400m<br>Ridgewater Racing Club<br>(Kestrel Park),<br>10 December 2016</p>
    </article>

    <article class="result" style="top:553px; height:167px;">
      <div class="result__label"><h2 class="result__headline">Velvet Harbor<br>beats Marindra<br>by 1.3L</h2></div>
      <p class="result__details">Class 6 Plate – 1300m<br>Ridgewater Racing Club<br>(Kestrel Park),<br>29 April 2017</p>
    </article>

    <article class="result" style="top:782px; height:167px;">
      <div class="result__label"><h2 class="result__headline">Velvet Harbor<br>wins by 2.3L</h2></div>
      <p class="result__details">Class 4 Handicap – 1400m<br>Ridgewater Racing Club (Hollins Vale),<br>23 November 2016</p>
    </article>

    <article class="result" style="top:1008px; height:166px;">
      <div class="result__label"><h2 class="result__headline">Velvet Harbor<br>wins on debut<br>at the Coral Bay!</h2></div>
      <p class="result__details">Maiden – 1000m Coral Bay<br>Turf Club,<br>23 October 2015</p>
    </article>
  </section>
</main>
</body>
</html>
```